CopperNomad Stretching and Strength

We need a application design for a our first IOS application. the goal of the application is to categorize stretching and strength routines for triathlon.

We would like to see designs that use the color orange.

The design of the application should be compliant with the last version of the IOS Mobile.

For this first design we need the folowing pages:

1- Sign up
2- Log in
3- Home
4- View Exercises
5- Do it
6- Profile

The description of each page is in the attached document.

We need a logo design for the application. The logo should express that mission of the application that is for stretch and strength training for Triathlon.

We will use https://plinthkit.example to develop the application, if you have any experience of the limitation that this technology have it will be a plus.

If you have any question please feel free to contact us.
Updates

Project Deadline Extended
Reason: We will extend the deadline to be sure that we select the best design from all of you. we will take the final decision next Tuesday.

Target Market(s)

The market for my aplicación is the Running a Triathlon world.

Logo Text

CopperNomad

Font styles to use
Serif

Colors
f37122
ffffff
dcdcdc

Requirements
Must have
• In some future we will add more features in the menu. We should considere it for the design.
• The designs should include all the screens in the power point.

```html
<!DOCTYPE html>
<html lang="en">
<head>
<meta charset="utf-8">
<title>CopperNomad – Navigation Drawer</title>
<link href="https://fonts.googleapis.com/css2?family=Roboto:wght@400;500;700&display=swap" rel="stylesheet">
<style>
  :root {
    --bg: #d5e3f0;
    --orange: #f37122;
    --white: #ffffff;
    --grey-light: #dcdcdc;
    --grey-panel: #eeeeee;
    --app-bg: #f1f1f1;
    --text-dark: #333333;
    --text-mid: #666666;
    --icon: #555555;
  }
  * { box-sizing: border-box; margin: 0; padding: 0; }
  html, body { width: 1200px; height: 1200px; overflow: hidden; background: var(--bg); font-family: 'Roboto', sans-serif; }
  .screen {
    position: absolute; left: 290px; top: 48px;
    width: 552px; height: 982px; overflow: hidden;
    background: var(--app-bg);
    transform: scale(1.1236); transform-origin: top left;
  }
  .abs { position: absolute; }

  /* right-hand app behind the drawer */
  .app-bar { left: 0; top: 0; width: 552px; height: 98px; background: var(--orange); }
  .status-right { left: 440px; top: 10px; color: var(--white); font-size: 16px; display: flex; align-items: center; gap: 6px; }
  .battery { width: 32px; height: 13px; border: 1.5px solid var(--white); border-radius: 3px; padding: 1px; position: relative; }
  .battery::before { content: ""; display: block; width: 100%; height: 100%; background: var(--white); border-radius: 1px; }
  .battery::after { content: ""; position: absolute; right: -4px; top: 3px; width: 2px; height: 5px; background: var(--white); }
  .menu-btn { left: 442px; top: 58px; width: 24px; }
  .menu-btn span { display: block; height: 2px; background: var(--white); margin-bottom: 5px; }
  .card { background: var(--white); left: 441px; width: 140px; box-shadow: 0 1px 3px rgba(0,0,0,.12); }
  .chart-card { top: 115px; height: 293px; }
  .chart-title { left: 74px; top: 14px; font-size: 15px; color: var(--orange); font-weight: 500; }
  .axis-label { left: 20px; top: 160px; font-size: 12px; color: var(--text-mid); transform: rotate(-90deg); transform-origin: left top; white-space: nowrap; }
  .axis-y { left: 56px; top: 85px; width: 1px; height: 166px; background: #cfcfcf; }
  .axis-x { left: 56px; top: 251px; width: 90px; height: 1px; background: #cfcfcf; }
  .legend { left: 83px; top: 153px; font-size: 12px; color: var(--text-mid); }
  .bar { left: 100px; top: 175px; width: 8px; height: 76px; background: var(--orange); }
  .tick { left: 39px; top: 260px; font-size: 12px; color: var(--text-mid); }
  .back-circle { left: 410px; top: 240px; width: 44px; height: 44px; border-radius: 50%; background: #dedede; }
  .history-card { top: 420px; height: 388px; }
  .card-title { left: 22px; top: 14px; font-size: 17px; color: var(--text-dark); font-weight: 500; }
  .title-rule { left: 92px; top: 25px; width: 60px; height: 1px; background: var(--grey-light); }
  .thumb { left: 23px; width: 82px; height: 76px; }
  .thumb-1 { top: 77px; background: linear-gradient(160deg, #9cb08a, #5d6f74 55%, #7c9a4f); }
  .thumb-2 { top: 220px; background: linear-gradient(150deg, #b8a79a, #3c5d84 45%, #b86a4e); }
  .thumb-3 { top: 362px; height: 26px; background: linear-gradient(90deg, #d8cfd0, #8a6e72 50%, #e5dfe0); }
  .row-rule { left: 0; width: 140px; height: 1px; background: #e6e6e6; }
  .sponsor-card { top: 818px; height: 147px; }
  .sponsor-box { left: 16px; top: 52px; width: 120px; height: 85px; border: 1px solid #e6e6e6; }
  .sponsor-name { left: 38px; top: 48px; font-size: 24px; font-weight: 700; color: #111111; white-space: nowrap; }

  /* drawer */
  .drawer { left: 0; top: 0; width: 430px; height: 982px; background: var(--white); box-shadow: 2px 0 6px rgba(0,0,0,.18); }
  .hero { left: 0; top: 0; width: 430px; height: 270px; background: radial-gradient(ellipse at 35% 45%, #8b7a60 0%, #5f6b3f 35%, #3d5a2a 65%, #2a3f22 100%); }
  .status-left { left: 7px; top: 10px; font-size: 16px; color: var(--white); display: flex; align-items: center; gap: 6px; }
  .dots { display: flex; gap: 2px; }
  .dots i { width: 8px; height: 8px; border-radius: 50%; border: 1px solid var(--white); }
  .dots i.on { background: var(--white); }
  .clock { left: 243px; top: 10px; font-size: 16px; color: var(--white); }
  .user-name { left: 11px; top: 223px; font-size: 23px; font-weight: 500; color: var(--white); text-shadow: 0 1px 3px rgba(0,0,0,.4); }
  .edit-btn { left: 380px; top: 222px; width: 35px; height: 35px; border-radius: 50%; background: var(--orange); display: flex; align-items: center; justify-content: center; box-shadow: 0 1px 3px rgba(0,0,0,.3); }

  .nav { left: 0; top: 289px; width: 430px; list-style: none; }
  .nav li { position: relative; height: 57.6px; display: flex; align-items: center; padding-left: 68px; font-size: 18px; }
  .nav .section { color: var(--text-dark); font-weight: 500; }
  .nav .sub { color: var(--text-mid); font-weight: 400; }
  .nav .active { color: var(--orange); }
  .nav svg { position: absolute; left: 14px; top: 17px; width: 24px; height: 24px; }

  .version { left: 0; top: 936px; width: 430px; height: 46px; background: var(--grey-panel); display: flex; align-items: center; justify-content: center; font-size: 15px; color: var(--text-dark); }
</style>
</head>
<body>
<div class="screen">
  <!-- app content behind drawer -->
  <div class="abs app-bar"></div>
  <div class="abs status-right">
    <svg width="10" height="16" viewBox="0 0 10 16" fill="none" stroke="#fff" stroke-width="1.4"><path d="M1 4l8 8-4 3V1l4 3-8 8"/></svg>
    <span>100%</span><span class="battery"></span>
  </div>
  <div class="abs menu-btn"><span></span><span></span><span></span></div>

  <div class="abs card chart-card">
    <div class="abs chart-title">Today</div>
    <div class="abs axis-label">Lorem ipsum</div>
    <div class="abs axis-y"></div>
    <div class="abs axis-x"></div>
    <div class="abs legend">Lorem</div>
    <div class="abs bar"></div>
    <div class="abs tick">10am</div>
  </div>
  <div class="abs back-circle"></div>

  <div class="abs card history-card">
    <div class="abs card-title">History</div>
    <div class="abs title-rule"></div>
    <div class="abs thumb thumb-1" role="img" aria-label="Group stretching outdoors on grass"></div>
    <div class="abs row-rule" style="top:203px"></div>
    <div class="abs thumb thumb-2" role="img" aria-label="Yoga class stretching on mats indoors"></div>
    <div class="abs row-rule" style="top:345px"></div>
    <div class="abs thumb thumb-3" role="img" aria-label="Workout session photo"></div>
  </div>

  <div class="abs card sponsor-card">
    <div class="abs card-title" style="top:14px">Sponsors</div>
    <div class="abs sponsor-box"></div>
    <div class="abs sponsor-name" style="top:100px">Stridewell</div>
  </div>

  <!-- navigation drawer -->
  <aside class="abs drawer">
    <div class="abs hero" role="img" aria-label="Profile photo of the user outdoors among trees"></div>
    <div class="abs status-left">
      <span class="dots"><i class="on"></i><i class="on"></i><i class="on"></i><i></i><i></i></span>
      <span>NOVA</span>
      <svg width="16" height="12" viewBox="0 0 16 12" fill="none" stroke="#fff" stroke-width="1.6"><path d="M1 4a10 10 0 0 1 14 0M3.5 6.5a6.5 6.5 0 0 1 9 0M6 9a3 3 0 0 1 4 0"/></svg>
    </div>
    <div class="abs clock">4:21 PM</div>
    <div class="abs user-name">Leo Marsh</div>
    <div class="abs edit-btn">
      <svg width="16" height="16" viewBox="0 0 16 16"><path d="M2 11.5V14h2.5l7.4-7.4-2.5-2.5L2 11.5zM13.7 4.8a.7.7 0 0 0 0-1L12.2 2.3a.7.7 0 0 0-1 0l-1.2 1.2 2.5 2.5 1.2-1.2z" fill="#fff"/></svg>
    </div>

    <ul class="abs nav">
      <li class="section">
        <svg viewBox="0 0 24 24" fill="var(--icon)"><circle cx="12" cy="7" r="4.5"/><path d="M4 21c0-5 3.5-7.5 8-7.5s8 2.5 8 7.5z"/></svg>Profile</li>
      <li class="section active">
        <svg viewBox="0 0 24 24" fill="var(--orange)"><path d="M12 3L1 12.5l1.5 1.5L4 12.8V21h6v-5h4v5h6v-8.2l1.5 1.2 1.5-1.5z"/></svg>Home</li>
      <li class="section">
        <svg viewBox="0 0 24 24" fill="var(--icon)"><path d="M13 4l5-2v18h-3v-7l-5 2-3 2-2-2 4-4z"/><circle cx="5" cy="13" r="2.2"/></svg>Stretching</li>
      <li class="sub">View Stretch</li>
      <li class="sub">View Routines</li>
      <li class="section">
        <svg viewBox="0 0 24 24" fill="var(--icon)"><path d="M9 4c3 0 4 2 3 4l-2 1c3 1 6 2 8 5 1 3-2 6-6 6H5c-2 0-3-2-1-3l5-1c2 0 3-1 2-2s-3-1-4 0L5 12c1-2 2-3 3-3-1-1-1-5 1-5z"/></svg>Strength</li>
      <li class="sub">View Exercises</li>
      <li class="sub">View Routines</li>
      <li class="section">
        <svg viewBox="0 0 24 24" fill="var(--icon)"><path d="M3 3h11v5h-2V5H7l4 3v11h1v-4h2v6h-3v2l-8-4z"/><path d="M15 10h4V7l4 4-4 4v-3h-4z"/></svg>Log Out</li>
    </ul>

    <div class="abs version">Version 0.0.1</div>
  </aside>
</div>
</body>
</html>
```